Business Card design

I would like to redo the business cards we have. I want a group card and then individual cards made for each doctor. I like the format of the card attached.

```html
<!DOCTYPE html>
<html lang="en">
<head>
<meta charset="utf-8">
<title>Riverbend Cancer Care – Business Cards</title>
<link href="https://fonts.googleapis.com/css2?family=Montserrat:wght@500;700;800&family=Open+Sans:wght@400;600;700&display=swap" rel="stylesheet">
<style>
  :root{
    --bg:#6f8d9d;
    --navy:#1d5b82;
    --sky:#3f95c6;
    --paper:#ffffff;
    --ink:#1d5b82;
    --grey:#6c7780;
    --rule:#dfe4e8;
  }
  *{margin:0;padding:0;box-sizing:border-box}
  html,body{width:1200px;height:2400px;overflow:hidden;background:var(--bg)}
  body{font-family:"Open Sans",Arial,sans-serif;color:var(--grey)}
  .set{position:relative;width:1200px;height:800px}
  .card{position:absolute;width:580px;height:330px;background:var(--paper);box-shadow:0 6px 18px rgba(0,0,0,.18)}
  .card--front{left:170px;top:70px;display:flex}
  .card--back{left:450px;top:430px;padding:34px 40px}

  .brand-panel{width:250px;height:100%;background:var(--navy);position:relative;padding:60px 26px 0}
  .brand{display:flex;align-items:center;gap:12px}
  .brand__square{width:26px;height:26px;background:var(--sky)}
  .brand__name{font-family:"Montserrat",Arial,sans-serif;font-weight:800;font-size:27px;line-height:1.05;color:#fff}
  .brand-tag{position:absolute;left:26px;right:26px;top:170px;height:24px;background:var(--sky);color:#fff;font-size:10px;font-weight:600;letter-spacing:.18em;text-transform:uppercase;display:flex;align-items:center;justify-content:center}

  .profile{flex:1;padding:50px 30px 0 30px}
  .profile__name{font-family:"Montserrat",Arial,sans-serif;font-weight:700;font-size:24px;line-height:1.15;color:var(--ink)}
  .profile__role{font-size:12px;font-weight:600;color:var(--sky);margin:8px 0 12px}
  .profile__line{font-size:11px;line-height:1.6}

  .roster{flex:1;padding:34px 24px 0 26px}
  .roster__item{margin-bottom:7px}
  .roster__name{font-family:"Montserrat",Arial,sans-serif;font-weight:700;font-size:13px;color:var(--ink)}
  .roster__role{display:block;background:var(--rule);font-size:9.5px;padding:1px 6px;margin-top:2px;width:180px}

  .locations__title{font-size:12px;font-weight:700;letter-spacing:.2em;color:var(--grey);margin-bottom:14px}
  .location{display:flex;gap:12px;margin-bottom:14px}
  .location__pin{flex:0 0 22px;height:22px}
  .location__name{font-size:12.5px;font-weight:700;color:var(--ink)}
  .location__detail{font-size:10.5px;line-height:1.45}
  .back-brand{position:absolute;right:34px;top:150px;display:flex;align-items:center;gap:8px}
  .back-brand__square{width:18px;height:18px;background:var(--navy)}
  .back-brand__name{font-family:"Montserrat",Arial,sans-serif;font-weight:800;font-size:15px;color:var(--navy)}
</style>
</head>
<body>

<!-- Individual card: Dana Whitfield -->
<section class="set">
  <article class="card card--front">
    <div class="brand-panel">
      <div class="brand"><span class="brand__square"></span><span class="brand__name">Riverbend</span></div>
      <div class="brand-tag">Cancer Care, PC</div>
    </div>
    <div class="profile">
      <h2 class="profile__name">Dana<br>Whitfield, M.D.</h2>
      <p class="profile__role">Medical Oncology</p>
      <p class="profile__line">12 Alder Park Drive, Suite 200</p>
      <p class="profile__line">Millbrook, New Jersey 07110</p>
      <p class="profile__line">Tel (973) 555-0142</p>
      <p class="profile__line">Fax (973) 555-0143</p>
    </div>
  </article>
  <article class="card card--back">
    <h3 class="locations__title">LOCATIONS</h3>
    <div class="location">
      <svg class="location__pin" viewBox="0 0 22 22"><circle cx="11" cy="11" r="11" fill="#1d5b82"/><path d="M11 5a4 4 0 0 0-4 4c0 3 4 8 4 8s4-5 4-8a4 4 0 0 0-4-4z" fill="#fff"/></svg>
      <div><p class="location__name">12 Alder Park Drive</p><p class="location__detail">Suite 200, Millbrook, New Jersey 07110<br>Tel (973) 555-0142 • Fax (973) 555-0143</p></div>
    </div>
    <div class="location">
      <svg class="location__pin" viewBox="0 0 22 22"><circle cx="11" cy="11" r="11" fill="#1d5b82"/><path d="M11 5a4 4 0 0 0-4 4c0 3 4 8 4 8s4-5 4-8a4 4 0 0 0-4-4z" fill="#fff"/></svg>
      <div><p class="location__name">Linden Ambulatory Care Pavilion</p><p class="location__detail">4 Cove Avenue, Suite 3, Fairhaven, New Jersey 07044<br>Tel (973) 555-0178 • Fax (973) 555-0179</p></div>
    </div>
    <div class="location">
      <svg class="location__pin" viewBox="0 0 22 22"><circle cx="11" cy="11" r="11" fill="#1d5b82"/><path d="M11 5a4 4 0 0 0-4 4c0 3 4 8 4 8s4-5 4-8a4 4 0 0 0-4-4z" fill="#fff"/></svg>
      <div><p class="location__name">640 East Maple Avenue</p><p class="location__detail">Westbrook, New Jersey 07205<br>Tel (908) 555-0191 • Fax (908) 555-0192</p></div>
    </div>
    <div class="back-brand"><span class="back-brand__square"></span><span class="back-brand__name">Riverbend</span></div>
  </article>
</section>

<!-- Individual card: Laura Prescott -->
<section class="set">
  <article class="card card--front">
    <div class="brand-panel">
      <div class="brand"><span class="brand__square"></span><span class="brand__name">Riverbend</span></div>
      <div class="brand-tag">Cancer Care, PC</div>
    </div>
    <div class="profile">
      <h2 class="profile__name">Laura<br>Prescott, M.D.</h2>
      <p class="profile__role">Hematology &amp; Oncology</p>
      <p class="profile__line">12 Alder Park Drive, Suite 200</p>
      <p class="profile__line">Millbrook, New Jersey 07110</p>
      <p class="profile__line">Tel (973) 555-0142</p>
      <p class="profile__line">Fax (973) 555-0143</p>
    </div>
  </article>
  <article class="card card--back">
    <h3 class="locations__title">LOCATIONS</h3>
    <div class="location">
      <svg class="location__pin" viewBox="0 0 22 22"><circle cx="11" cy="11" r="11" fill="#1d5b82"/><path d="M11 5a4 4 0 0 0-4 4c0 3 4 8 4 8s4-5 4-8a4 4 0 0 0-4-4z" fill="#fff"/></svg>
      <div><p class="location__name">12 Alder Park Drive</p><p class="location__detail">Suite 200, Millbrook, New Jersey 07110<br>Tel (973) 555-0142 • Fax (973) 555-0143</p></div>
    </div>
    <div class="location">
      <svg class="location__pin" viewBox="0 0 22 22"><circle cx="11" cy="11" r="11" fill="#1d5b82"/><path d="M11 5a4 4 0 0 0-4 4c0 3 4 8 4 8s4-5 4-8a4 4 0 0 0-4-4z" fill="#fff"/></svg>
      <div><p class="location__name">Linden Ambulatory Care Pavilion</p><p class="location__detail">4 Cove Avenue, Suite 3, Fairhaven, New Jersey 07044<br>Tel (973) 555-0178 • Fax (973) 555-0179</p></div>
    </div>
    <div class="location">
      <svg class="location__pin" viewBox="0 0 22 22"><circle cx="11" cy="11" r="11" fill="#1d5b82"/><path d="M11 5a4 4 0 0 0-4 4c0 3 4 8 4 8s4-5 4-8a4 4 0 0 0-4-4z" fill="#fff"/></svg>
      <div><p class="location__name">640 East Maple Avenue</p><p class="location__detail">Westbrook, New Jersey 07205<br>Tel (908) 555-0191 • Fax (908) 555-0192</p></div>
    </div>
    <div class="back-brand"><span class="back-brand__square"></span><span class="back-brand__name">Riverbend</span></div>
  </article>
</section>

<!-- Group card -->
<section class="set">
  <article class="card card--front">
    <div class="brand-panel">
      <div class="brand"><span class="brand__square"></span><span class="brand__name">Riverbend</span></div>
      <div class="brand-tag">Cancer Care, PC</div>
    </div>
    <div class="roster">
      <div class="roster__item"><p class="roster__name">James R. Colton, M.D.</p><span class="roster__role">Medical Oncology</span></div>
      <div class="roster__item"><p class="roster__name">Dana Whitfield, M.D.</p><span class="roster__role">Medical Oncology</span></div>
      <div class="roster__item"><p class="roster__name">Laura Prescott, M.D.</p><span class="roster__role">Hematology &amp; Oncology</span></div>
      <div class="roster__item"><p class="roster__name">Owen Hartley, M.D.</p><span class="roster__role">Radiation Oncology</span></div>
      <div class="roster__item"><p class="roster__name">Nina Castell, M.D.</p><span class="roster__role">Hematology</span></div>
    </div>
  </article>
  <article class="card card--back">
    <h3 class="locations__title">LOCATIONS</h3>
    <div class="location">
      <svg class="location__pin" viewBox="0 0 22 22"><circle cx="11" cy="11" r="11" fill="#1d5b82"/><path d="M11 5a4 4 0 0 0-4 4c0 3 4 8 4 8s4-5 4-8a4 4 0 0 0-4-4z" fill="#fff"/></svg>
      <div><p class="location__name">12 Alder Park Drive</p><p class="location__detail">Suite 200, Millbrook, New Jersey 07110<br>Tel (973) 555-0142 • Fax (973) 555-0143</p></div>
    </div>
    <div class="location">
      <svg class="location__pin" viewBox="0 0 22 22"><circle cx="11" cy="11" r="11" fill="#1d5b82"/><path d="M11 5a4 4 0 0 0-4 4c0 3 4 8 4 8s4-5 4-8a4 4 0 0 0-4-4z" fill="#fff"/></svg>
      <div><p class="location__name">Linden Ambulatory Care Pavilion</p><p class="location__detail">4 Cove Avenue, Suite 3, Fairhaven, New Jersey 07044<br>Tel (973) 555-0178 • Fax (973) 555-0179</p></div>
    </div>
    <div class="location">
      <svg class="location__pin" viewBox="0 0 22 22"><circle cx="11" cy="11" r="11" fill="#1d5b82"/><path d="M11 5a4 4 0 0 0-4 4c0 3 4 8 4 8s4-5 4-8a4 4 0 0 0-4-4z" fill="#fff"/></svg>
      <div><p class="location__name">640 East Maple Avenue</p><p class="location__detail">Westbrook, New Jersey 07205<br>Tel (908) 555-0191 • Fax (908) 555-0192</p></div>
    </div>
    <div class="back-brand"><span class="back-brand__square"></span><span class="back-brand__name">Riverbend</span></div>
  </article>
</section>

</body>
</html>
```